brix4lane

i want to ues this logo and the same colors used on the business card

cleaning & service

Industry/Entity Type

Business

Contact Information for Business Card

Font styles to use
Serif
Sans Serif
Decorative
Script

Colors
add136
0692cd
000000
5c5c5c
fbfbfb

Requirements
Must have
• cleaning things

```html
<!DOCTYPE html>
<html lang="en">
<head>
<meta charset="utf-8">
<title>brix4lane business card</title>
<link href="https://fonts.googleapis.com/css2?family=Roboto:wght@400;500&display=swap" rel="stylesheet">
<style>
  :root {
    --green: #add136;
    --blue: #0692cd;
    --sky: #2fa3dc;
    --black: #1e1e1e;
    --grey: #5c5c5c;
    --paper: #fbfbfb;
    --backdrop: #e9e6e1;
  }
  html, body {
    margin: 0;
    width: 1200px;
    height: 923px;
    overflow: hidden;
    background: var(--backdrop);
    font-family: "Roboto", Arial, sans-serif;
  }
  .card {
    position: absolute;
    left: 75px;
    top: 161px;
    width: 1050px;
    height: 600px;
    background: var(--paper);
    box-shadow: 0 10px 30px rgba(0,0,0,0.18);
    overflow: hidden;
  }
  .card-wave {
    position: absolute;
    inset: 0;
    width: 100%;
    height: 100%;
  }
  .brand {
    position: absolute;
    left: 170px;
    top: 130px;
    display: flex;
    align-items: center;
    gap: 14px;
  }
  .brand-dot {
    width: 22px;
    height: 22px;
    border-radius: 50%;
    background: var(--green);
  }
  .brand-name {
    font-size: 58px;
    font-weight: 500;
    color: var(--blue);
    letter-spacing: 0.5px;
  }
  .holder {
    position: absolute;
    right: 80px;
    top: 235px;
    text-align: right;
  }
  .holder-name {
    font-size: 34px;
    color: var(--paper);
    line-height: 1.1;
  }
  .holder-role {
    font-size: 24px;
    color: var(--green);
    margin-top: 4px;
  }
  .contacts {
    position: absolute;
    left: 120px;
    bottom: 70px;
    list-style: none;
    margin: 0;
    padding: 0;
  }
  .contact {
    display: flex;
    align-items: center;
    gap: 18px;
    font-size: 31px;
    color: var(--paper);
    margin-top: 14px;
  }
  .contact svg { width: 28px; height: 28px; flex: none; }
</style>
</head>
<body>
  <div class="card">
    <svg class="card-wave" viewBox="0 0 1050 600" preserveAspectRatio="none" aria-hidden="true">
      <path class="wave-fill" fill="var(--black)"
            d="M0,360 C260,352 440,320 540,235 C640,150 790,100 1050,90 L1050,600 L0,600 Z"/>
      <path class="wave-blue" fill="var(--sky)"
            d="M0,324 C220,316 390,294 490,240 C515,226 535,212 552,196 C505,262 440,300 360,318 C250,340 120,344 0,346 Z"/>
      <path class="wave-black" fill="var(--black)"
            d="M110,304 C300,290 440,265 520,200 C630,125 790,85 1050,80 L1050,38 C790,45 610,90 505,175 C430,240 300,282 110,304 Z"/>
    </svg>

    <div class="brand">
      <span class="brand-dot"></span>
      <span class="brand-name">brix4lane</span>
    </div>

    <div class="holder">
      <div class="holder-name">Your Name</div>
      <div class="holder-role">Owner</div>
    </div>

    <ul class="contacts">
      <li class="contact">
        <svg viewBox="0 0 24 24" aria-hidden="true"><path fill="var(--green)" d="M6.6 10.8c1.4 2.8 3.8 5.1 6.6 6.6l2.2-2.2c.3-.3.7-.4 1-.2 1.1.4 2.3.6 3.6.6.6 0 1 .4 1 1V20c0 .6-.4 1-1 1C10.6 21 3 13.4 3 4c0-.6.4-1 1-1h3.5c.6 0 1 .4 1 1 0 1.3.2 2.5.6 3.6.1.3 0 .7-.2 1z"/></svg>
        <span>(123) 123-1234</span>
      </li>
      <li class="contact">
        <svg viewBox="0 0 24 24" aria-hidden="true"><path fill="var(--green)" d="M2 5h20v14H2z"/><path d="M2 5l10 8 10-8" fill="none" stroke="var(--black)" stroke-width="1.6"/></svg>
        <span>hello@brix4lane.com</span>
      </li>
    </ul>
  </div>
</body>
</html>
```